Apply Existing Website Design to Pellmoor-Made Tele-Wellness App (UX/UI Work)

We’re looking for a highly skilled UX/UI designer to translate our existing website design into an intuitive, beautiful mobile app interface for our Pellmoor-developed tele-wellness platform. Hoping this designer will stay onboard with us for future work.

Scope of Work:
    •    Review our existing website design (style, colors, typography, components)
    •    Apply the same visual language to our mobile app screens
    •    Ensure consistent, user-friendly experience across the app
    •    Deliver high-fidelity mockups and design assets (preferably in Figma)
    •    Minimal UX rethinking may be needed to optimize for mobile, but the core brand and design system are already established

What We Provide:
    •    Access to the existing website design (including any style guides or component libraries)
    •    Wireframes or a basic functional map of the app screens
    •    Clear guidelines on branding and user flows

Ideal Candidate:
    •    Strong portfolio of mobile app design, especially healthcare/wellness preferred
    •    Proven experience in adapting web designs for mobile apps
    •    Expertise with Figma or comparable tools
    •    Attention to detail and commitment to brand consistency
    •    Ability to deliver quickly while maintaining quality

Deliverables:
    •    Complete set of high-fidelity, mobile-optimized app screens
    •    Organized design file (Figma preferred) ready for developer handoff
    •    Design assets as needed (icons, images, components)

Timeline:
    •    Estimated 1 week for initial delivery, with room for revisions

```html
<!DOCTYPE html>
<html lang="en">
<head>
<meta charset="utf-8">
<title>Auvela – Tele-Wellness Web &amp; App Design</title>
<link href="https://fonts.googleapis.com/css2?family=Crimson+Pro:wght@400;500&family=Inter:wght@400;500;600&display=swap" rel="stylesheet">
<style>
:root{
  --board:#6b3d14;
  --peach:#f8c79b;
  --peach-soft:#fbd9b9;
  --peach-deep:#eeaa6e;
  --paper:#ebebeb;
  --paper-2:#f1f1f1;
  --white:#ffffff;
  --ink:#2c2c2c;
  --ink-2:#5a5a5a;
  --muted:#8a8a8a;
  --line:#d6d6d6;
}
*{box-sizing:border-box;margin:0;padding:0}
html,body{width:1200px;height:4065px;overflow:hidden}
body{background:var(--board);font-family:"Inter",sans-serif;color:var(--ink);position:relative}
.serif{font-family:"Crimson Pro",serif;font-weight:400}

/* ---------- desktop page ---------- */
.desktop{position:absolute;left:382px;top:60px;width:698px;height:3920px;background:var(--paper);overflow:hidden}
.sec{position:absolute;left:0;width:698px}
.pill-btn{display:inline-block;background:var(--peach);color:var(--ink);border-radius:20px;font-size:8px;letter-spacing:.06em;padding:8px 30px}

.hero{top:0;height:327px;background:radial-gradient(ellipse at 78% 45%,#e8ece4 0,#b9c2b1 9%,#3e4d34 24%,#1e2a19 55%,#111a0f 100%);color:var(--white)}
.nav{position:absolute;left:65px;right:30px;top:14px;display:flex;align-items:center}
.logo{font-family:"Inter",sans-serif;font-weight:500;font-size:22px;letter-spacing:.04em;color:var(--peach-soft)}
.nav ul{margin-left:auto;display:flex;gap:22px;list-style:none;font-size:7.5px;align-items:center}
.nav .outline{border:1px solid var(--white);border-radius:12px;padding:5px 10px}
.hero h1{position:absolute;left:65px;top:126px;font-size:19px;line-height:1.2}
.hero .lede{position:absolute;left:65px;top:178px;font-size:9px;line-height:1.7;color:#e4e4e4}
.hero .dev{position:absolute;left:65px;top:238px;font-size:9.5px;font-weight:600}
.hero .pill-btn{position:absolute;left:65px;top:263px;padding:8px 40px}

.trusted{top:327px;height:384px}
.trusted .head{position:absolute;left:65px;top:36px;font-size:15px}
.trusted .head b{font-family:"Inter",sans-serif;font-weight:600;font-size:15px}
.trusted .sub{position:absolute;left:65px;top:66px;font-size:7px;color:var(--muted)}
.bubble{position:absolute;top:96px;width:212px;height:206px;border-radius:50%;background:var(--peach);text-align:center;padding:18px 26px 0}
.avatar{width:32px;height:32px;border-radius:50%;background:linear-gradient(#cfcfcf,#8f8f8f);margin:0 auto 6px;border:2px solid var(--white)}
.bubble h4{font-size:8px;font-weight:500;line-height:1.3;margin-bottom:5px}
.bubble p{font-size:6.8px;line-height:1.45;color:var(--ink-2)}
.bubble .who{margin-top:8px;font-size:7px}
.trusted .stat{position:absolute;left:0;right:0;top:328px;text-align:center;font-size:11px}
.trusted .stat b{font-weight:600;font-size:13px}

.tested{top:711px;height:490px;background:var(--paper-2)}
.ctitle{text-align:center;font-size:18px}
.csub{text-align:center;font-size:7px;color:var(--muted);margin-top:10px}
.tested .ctitle{margin-top:32px}
.cards3{display:flex;gap:18px;margin:30px 65px 0;}
.tcard{flex:1;background:var(--white);height:238px;padding:18px 14px;text-align:center}
.tcard svg{width:32px;height:32px;margin-bottom:18px}
.tcard h4{font-size:8px;font-weight:500;line-height:1.35;margin-bottom:12px}
.tcard p{font-size:6.8px;line-height:1.55;color:var(--ink-2)}
.tested .cta{text-align:center;margin-top:32px}
.tested .cta small{display:block;font-size:6px;color:var(--muted);margin-top:10px}

.diff{top:1201px;height:694px}
.diff .lt{position:absolute;left:60px;top:38px;font-size:16px}
.tabs3{position:absolute;left:60px;top:80px;display:flex;gap:18px}
.tab{width:178px;height:74px;background:var(--peach);border-radius:12px 30px 12px 12px;display:flex;align-items:center;gap:10px;padding:0 12px}
.tab .ic{width:34px;height:34px;border-radius:50%;background:var(--white);flex:none}
.tab h5{font-size:8px;font-weight:500;line-height:1.3}
.tab p{font-size:6px;color:var(--ink-2);margin-top:3px}
.orbit{position:absolute;left:0;top:0;width:698px;height:694px}
.core{position:absolute;left:52px;top:286px;width:262px;height:262px;border-radius:50%;background:var(--paper-2);text-align:center;padding:46px 34px 0;box-shadow:0 0 0 1px #e2e2e2}
.core h5{font-size:8px;font-weight:500;margin-bottom:14px}
.core h6{font-size:7px;font-weight:500;margin:10px 0 6px}
.core p{font-size:6.6px;line-height:1.55;color:var(--muted)}
.lead{position:absolute;left:268px;top:185px;width:230px;height:52px;border-radius:26px;background:var(--white);display:flex;align-items:center;gap:10px;padding-left:10px;font-size:8px}
.node{position:absolute;display:flex;align-items:center;gap:10px;font-size:8px;white-space:nowrap}
.node i,.lead i{width:36px;height:36px;border-radius:50%;background:var(--peach);display:block;flex:none;box-shadow:0 0 0 4px var(--paper)}
.steps{top:1895px;height:229px}
.steps .rule{position:absolute;left:60px;right:60px;height:1px;background:var(--line)}
.step{position:absolute;display:flex;gap:12px;width:260px}
.num{width:58px;height:58px;border-radius:50%;background:var(--white);box-shadow:6px 0 0 var(--peach-soft);flex:none;display:flex;align-items:center;justify-content:center;font-family:"Crimson Pro",serif;font-size:34px;color:#bdbdbd}
.step h5{font-size:8.5px;font-weight:500;margin:12px 0 6px}
.step p{font-size:6.6px;line-height:1.55;color:var(--ink-2)}

.experts{top:2124px;height:316px}
.experts .ctitle{margin-top:28px}
.exrow{display:flex;gap:14px;margin:30px 70px 0}
.excard{flex:1;height:152px;background:var(--white);text-align:center;padding-top:14px}
.excard .avatar{width:62px;height:62px;margin-bottom:12px}
.excard h5{font-size:7.5px;font-weight:500;margin-bottom:6px}
.excard p{font-size:6.5px;color:var(--ink-2);line-height:1.6}

.compare{top:2440px;height:450px;background:var(--paper-2)}
.compare .lt{position:absolute;left:65px;top:48px;font-size:16px}
.compare .ls{position:absolute;left:65px;top:76px;font-size:7px;color:var(--muted)}
.cmp-table{position:absolute;left:65px;top:106px;width:568px;border-collapse:separate;border-spacing:6px 13px;font-size:6.8px}
.cmp-table th{font-weight:400;font-size:6px;color:var(--ink-2);height:22px;vertical-align:bottom}
.cmp-table th.brand{font-size:11px;color:var(--peach-deep);letter-spacing:.05em}
.cmp-table td{height:31px;text-align:center;background:var(--white);color:var(--ink-2)}
.cmp-table td.row{background:none;text-align:left;width:110px;color:var(--ink)}
.cmp-table td.us,.cmp-table td.hi{background:var(--peach)}

.backed{top:2890px;height:181px;border-bottom:1px solid var(--line)}
.backed h3{position:absolute;left:65px;top:64px;font-size:17px;line-height:1.15;width:240px}
.badges{position:absolute;left:330px;top:30px;display:flex;gap:12px}
.badge{width:98px;height:112px;background:var(--white);text-align:center;padding-top:14px;font-size:6.8px;line-height:1.45}
.badge .mk{width:42px;height:42px;border-radius:50%;background:#b9c6d8;margin:0 auto 10px}
.badge .mk.sq{border-radius:2px;background:#2a3f7a;width:32px}

.bio{top:3071px;height:316px}
.chips{position:absolute;left:65px;top:36px;display:flex;gap:8px}
.chip{width:106px;height:30px;border-radius:15px;background:var(--white);font-size:6px;text-align:center;display:flex;align-items:center;justify-content:center;line-height:1.3;padding:0 6px}
.chip.on{background:var(--peach)}
.bio .pic{position:absolute;left:65px;top:100px;width:283px;height:172px;border-radius:0 46px 0 46px;background:radial-gradient(circle at 60% 45%,#f3c57a 0,#b2762f 25%,#5a3413 60%,#2a1707 100%)}
.bio h4{position:absolute;left:380px;top:138px;font-size:10px;font-weight:500}
.bio p{position:absolute;left:380px;top:160px;width:250px;font-size:6.8px;line-height:1.6;color:var(--ink-2)}

.quote{top:3387px;height:505px;background:radial-gradient(ellipse at 85% 40%,#f4e7ee 0,#d7aac0 14%,#5d3a4a 35%,#27261a 70%,#16170f 100%);color:var(--white)}
.qmark{position:absolute;left:329px;top:38px;width:40px;height:40px;border-radius:50%;background:var(--peach);opacity:.9}
.glass{position:absolute;background:rgba(255,255,255,.32);border-radius:14px;color:var(--ink)}
.g1{left:106px;top:56px;width:484px;height:202px;text-align:center;padding:64px 40px 0}
.g1 p{font-size:8.5px;line-height:1.6}
.g1 h3{font-size:19px;line-height:1.5;margin-top:10px}
.g1 .sig{position:absolute;right:40px;bottom:26px;font-size:7px}
.g2{left:106px;top:282px;width:484px;height:90px;padding:26px 22px;font-size:7.5px;line-height:1.8}
.contact{position:absolute;left:65px;top:418px}
.contact h3{font-family:"Inter",sans-serif;font-weight:500;font-size:17px;margin-bottom:22px}
.contact p{font-size:7px;margin-bottom:12px}
.foot{top:3892px;height:87px;background:#3a3a3a;color:#eee;font-size:6.8px}
.stats{display:flex;justify-content:space-around;padding:8px 40px;border-bottom:1px solid #555}
.flinks{display:flex;justify-content:space-around;padding:8px 120px;font-size:6.5px}
.copy{position:absolute;left:65px;top:60px;font-size:6.5px}

/* ---------- mobile page (drawn at 2x, scaled down) ---------- */
.mobile{position:absolute;left:182px;top:60px;width:350px;height:4564px;transform:scale(.5);transform-origin:0 0;background:var(--paper);overflow:hidden}
.ms{position:relative;overflow:hidden;padding:0 22px}
.m-hero{height:700px;background:radial-gradient(ellipse at 60% 30%,#e9ede6 0,#aab6a0 12%,#3b4a30 32%,#1a2515 70%);color:var(--white);padding:20px 24px}
.m-hero .logo{font-size:22px}
.burger{position:absolute;right:24px;top:26px;width:18px;height:12px;border-top:2px solid #fff;border-bottom:2px solid #fff}
.burger::after{content:"";position:absolute;left:0;right:0;top:3px;border-top:2px solid #fff}
.m-hero h1{font-size:56px;line-height:.9;margin-top:70px}
.m-hero h2{font-size:30px;margin-top:18px}
.m-hero p{font-size:13px;line-height:1.35;margin-top:10px}
.m-hero b{display:block;font-size:13px;margin-top:22px}
.m-hero .pill-btn{position:absolute;left:86px;top:592px;font-size:12px;padding:10px 60px}
.sm{font-size:10px;line-height:1.5;color:var(--ink-2)}
.mt{font-size:22px;text-align:center;line-height:1.1}

.m-trust{height:460px;padding-top:16px}
.m-bubble{width:270px;height:270px;border-radius:50%;background:var(--peach);margin:20px auto 8px;padding:22px 34px;text-align:center}
.m-bubble .avatar{width:40px;height:40px}
.m-bubble h4{font-size:11px;font-weight:500;margin-bottom:8px}
.m-bubble p{font-size:9.5px;line-height:1.45;color:var(--ink-2)}
.dots{display:flex;justify-content:center;gap:5px;margin:8px 0}
.dots i{width:6px;height:6px;border-radius:50%;background:#bbb}
.dots i.on{background:#555}

.m-tested{height:800px;padding-top:18px}
.m-card{background:var(--white);margin:14px 0;height:178px;padding:16px 20px}
.m-card .ic{width:24px;height:24px;border-radius:50%;background:var(--peach-soft)}
.m-card h4{font-size:11px;font-weight:500;margin:8px 0}
.m-card p{font-size:9.5px;line-height:1.45;color:var(--ink-2)}

.m-tabs{height:300px;padding-top:10px}
.m-tab{height:52px;background:var(--peach);border-radius:12px;margin:12px 0;display:flex;align-items:center;gap:12px;padding:0 12px;font-size:11px}
.m-tab i{width:30px;height:30px;border-radius:50%;background:var(--white);flex:none}
.m-tab small{display:block;font-size:8px;color:var(--ink-2)}

.m-orbit{height:460px}
.m-core{position:absolute;left:85px;top:110px;width:180px;height:180px;border-radius:50%;background:var(--paper-2);border:5px solid var(--peach);padding:28px 16px;text-align:center;font-size:10px;line-height:1.4}
.m-node{position:absolute;width:90px;text-align:center;font-size:8.5px;line-height:1.25}
.m-node i{display:block;width:24px;height:24px;border-radius:50%;background:var(--peach);margin:4px auto}

.m-steps{height:300px;padding-top:10px}
.m-step{display:flex;align-items:center;gap:10px;background:var(--peach-soft);border-radius:26px;height:56px;margin:12px 0;padding:0 12px;font-size:10px;width:240px}
.m-step.r{margin-left:66px;flex-direction:row-reverse;text-align:right}
.m-step span{width:34px;height:34px;border-radius:50%;background:var(--white);display:flex;align-items:center;justify-content:center;font-size:14px;color:#aaa;flex:none}
.m-step small{display:block;font-size:7.5px;color:var(--ink-2)}

.m-experts{height:330px;padding-top:14px;text-align:center}
.m-car{position:relative;height:140px;margin:16px -22px 0}
.m-car div{position:absolute;top:0;height:140px;background:var(--white);font-size:9px;padding-top:14px}
.m-car .avatar{width:44px;height:44px;margin-bottom:8px}

.m-compare{height:500px;padding-top:14px;text-align:center}
.m-table{width:100%;border-collapse:separate;border-spacing:3px 5px;font-size:7.5px;margin-top:8px}
.m-table th{font-weight:400;font-size:7px;height:26px;vertical-align:bottom}
.m-table td{height:44px;background:var(--white);text-align:center}
.m-table td.row{background:none;text-align:left;font-size:8px}
.m-table td.us,.m-table td.hi{background:var(--peach)}

.m-backed{height:190px;padding-top:14px;text-align:center}
.m-badges{display:flex;justify-content:space-around;margin-top:16px;font-size:8px;line-height:1.3}
.m-badges .mk{width:36px;height:36px;border-radius:50%;background:#b9c6d8;margin:0 auto 6px}

.m-chips{height:110px;display:flex;flex-wrap:wrap;gap:8px;padding-top:14px;justify-content:center}
.m-chips span{height:24px;border-radius:12px;background:var(--white);font-size:7px;padding:0 10px;display:flex;align-items:center}
.m-chips span.on{background:var(--peach)}

.m-bio{height:100px;display:flex;gap:12px;align-items:center}
.m-bio .pic{width:110px;height:80px;flex:none;border-radius:0 24px 0 24px;background:radial-gradient(circle at 40% 50%,#f3c57a,#6a3d12 60%,#2a1707)}
.m-bio h4{font-size:10px;font-weight:500;margin-bottom:4px}
.m-bio p{font-size:7.5px;line-height:1.4;color:var(--ink-2)}

.m-quote{height:314px;background:radial-gradient(ellipse at 60% 30%,#e8d6de,#6a4656 40%,#1f1f16 85%);padding:30px 22px;color:var(--white)}
.m-quote .gl{background:rgba(255,255,255,.32);border-radius:12px;padding:18px;font-size:10px;text-align:center;color:var(--ink);line-height:1.4}
.m-quote .gl h3{font-size:16px;margin-top:6px}
.m-quote .ct{margin-top:30px;font-size:9px;line-height:1.8}
.m-quote .ct b{display:block;font-size:14px;font-weight:500}
</style>
</head>
<body>

<!-- Mobile screen -->
<div class="mobile">
  <div class="ms m-hero" role="img" aria-label="Photo of a white blossom on dark green leaves">
    <div class="logo">AUVELA</div><span class="burger"></span>
    <h1 class="serif">Holistic-<br>Doctor led<br>care.</h1>
    <h2 class="serif">Pay as you like</h2>
    <p>Evidence based care with heart<br>Tailored only for you<br>Tele-Wellness</p>
    <b>Developed at Pellmoor</b>
    <span class="pill-btn">Book Now</span>
  </div>

  <div class="ms m-trust">
    <div style="font-size:13px"><span class="serif">Trusted by :</span> <b>Northfield Outfitters</b></div>
    <div class="sm">Pioneers in corporate wellness: A Better Way To Grow</div>
    <div class="m-bubble"><div class="avatar"></div><h4>Chief Strategy Officer,<br>National Tech Firm</h4><p>For the first time in 20 years of nonstop output I found a wellness system that didn't just slow me down—it woke me up. Auvela's personalized protocols gave me energy I didn't know I was missing, and helped me show up sharper, calmer, and more focused than ever before.</p><p style="margin-top:8px">Daniel</p></div>
    <div class="dots"><i></i><i class="on"></i><i></i></div>
    <div class="sm" style="text-align:center"><b>55</b> Million Bio-Markers analysed</div>
  </div>

  <div class="ms m-tested">
    <div class="mt serif">Time Tested and<br>Results Driven</div>
    <p class="sm" style="text-align:center;margin-top:6px">We get it. You've tried the threads, the threads on the threads. It's time for something real and built around you, clarity is a form of care.</p>
    <div class="m-card"><span class="ic" style="display:block"></span><h4>Conflicted by fad-driven advice and endless tests without real insight?</h4><p>Auvela cuts through the noise with time-tested, evidence-based care and real credentials—thousands of years of wisdom versus a few years of fragmented information in holistic medicine.</p></div>
    <div class="m-card"><span class="ic" style="display:block"></span><h4>Tired of one-size-fits-all supplements?</h4><p>At Auvela, every formula is tailored to your unique mind-body type. No algorithms. No shortcuts. Just real doctors creating real, time-tested protocols—just for you. You deserve precision—not guesswork.</p></div>
    <div class="m-card"><span class="ic" style="display:block"></span><h4>Being overcharged by unqualified, self-professed experts?</h4><p>The human psychology of valuing only that which we pay a lot for can be remedied with proven results. By setting an example—by making high-quality health care available to everyone. We hope, that most will benefit.</p></div>
    <div style="text-align:center"><span class="pill-btn">Book Now</span><div class="sm" style="font-size:8px;margin-top:6px">Three minutes. No commitment. Much clarity.</div></div>
  </div>

  <div class="ms m-tabs">
    <div class="mt serif">The Auvela Difference</div>
    <div class="m-tab"><i></i><div>Precision You Can Trust<small>Doctors cross-trained in time tested and modern science</small></div></div>
    <div class="m-tab"><i></i><div>Care You Can Feel<small>Plans crafted around your whole self &amp; labs</small></div></div>
    <div class="m-tab"><i></i><div>Ethics You Can Stand Behind<small>Fair-trade sourcing, real transparency</small></div></div>
  </div>

  <div class="ms m-orbit">
    <div class="m-node" style="left:20px;top:70px"><i></i>1. Clinical Precision</div>
    <div class="m-node" style="left:60px;top:10px">2. High-Touch Personalization<i></i></div>
    <div class="m-node" style="left:180px;top:10px">3. No Harmful Cross-Reactions<i></i></div>
    <div class="m-node" style="left:250px;top:60px">4. Science-Guided Herbalism<i></i></div>
    <div class="m-core"><b>1. Clinical Precision</b><br>What We Do<br><span style="font-size:8px;color:#888">Ayurvedic doctors trained in classical and integrative science.</span><br>Why It Matters</div>
    <div class="m-node" style="left:250px;top:300px"><i></i>7. Evidence-Informed Guidance</div>
    <div class="m-node" style="left:130px;top:340px"><i></i>6. Global Standard Sourcing</div>
    <div class="m-node" style="left:10px;top:300px"><i></i>5. Regulatory Integrity</div>
  </div>

  <div class="ms m-steps">
    <div class="m-step"><span>01</span><div>Book<small>Book now and fill out your secured details</small></div></div>
    <div class="m-step r"><span>02</span><div>Video Call<small>Video chat with your specialist</small></div></div>
    <div class="m-step"><span>03</span><div>Get Care + Unlimited Text<small>Customized diet, yoga &amp; meditation plans</small></div></div>
    <div class="m-step r"><span>04</span><div>Monthly Video Follow Up<small>Essential care takes persistence</small></div></div>
  </div>

  <div class="ms m-experts">
    <div class="mt serif">The Auvela Difference</div>
    <p class="sm" style="margin-top:6px">We get it. You've tried the threads, the threads on the threads. It's time for something real and built around you, clarity is a form of care.</p>
    <div class="m-car">
      <div style="left:-60px;width:80px"></div>
      <div style="left:50px;width:250px"><span class="avatar" style="display:block"></span>Dr. Sara Lindqvist<br><span class="sm" style="font-size:8px">MBBS<br>BAMS<br>Oncology Director</span></div>
      <div style="left:330px;width:80px"></div>
    </div>
    <div class="dots"><i></i><i class="on"></i><i></i></div>
  </div>

  <div class="ms m-compare">
    <div class="mt serif">How We Compare</div>
    <div class="sm">No hidden fees, ever.</div>
    <table class="m-table">
      <tr><th></th><th style="color:var(--peach-deep)">AUVELA</th><th>Our Compet-itor</th><th>Others</th><th>Nutrit-ionist</th><th>Bio-marker Result</th><th>Gene Result</th></tr>
      <tr><td class="row">Integrative Doctors</td><td class="us">Included</td><td>X</td><td>$500 visit</td><td>X</td><td>X</td><td>X</td></tr>
      <tr><td class="row">1 on 1 Video</td><td class="us">Included</td><td>X</td><td>$500 visit</td><td class="hi">✓</td><td>X</td><td>X</td></tr>
      <tr><td class="row">Unlimited Text</td><td class="us">Included</td><td>X</td><td>X</td><td>X</td><td>X</td><td>X</td></tr>
      <tr><td class="row">Time Tested</td><td class="us">Included</td><td>Infre-quently</td><td>X</td><td>X</td><td>X</td><td>X</td></tr>
      <tr><td class="row">200 Bio marker tested</td><td class="us">1st 100 $100</td><td>$300 min</td><td>$250 min</td><td>X</td><td class="hi">✓</td><td>X</td></tr>
      <tr><td class="row">Usage Rate</td><td class="us">98%</td><td>20% High</td><td>✓</td><td class="hi">✓</td><td class="hi">✓</td><td class="hi">✓</td></tr>
    </table>
  </div>

  <div class="ms m-backed">
    <div class="mt serif" style="font-size:17px">Backed by Expertise, Certified<br>for Safety. Trusted by design</div>
    <div class="m-badges"><div><div class="mk"></div>ISO 22000 &amp; EU<br>herbal standards</div><div><div class="mk" style="background:#2a3f7a"></div>GDPR-compliant<br>data privacy</div><div><div class="mk" style="border-radius:2px;background:#2a3f7a;width:28px"></div>Every supplement<br>screened</div></div>
  </div>

  <div class="ms m-chips">
    <span>Do You Need Labs for HRT?</span><span class="on">Bio markers and holistic integration</span><span>How We Personalize Every Formula</span><span>Prevent contraindicated therapies</span><span>Mislabeled Therapies to Watch Out For</span>
  </div>

  <div class="ms m-bio">
    <div class="pic" role="img" aria-label="Photo of cupped hands releasing golden sparkles"></div>
    <div><h4>Bio markers and holistic integration</h4><p>Bio markers are often not time tested nor accurate for hormones, which fluctuate day to day. We pair lab markers with time tested methods.</p></div>
  </div>

  <div class="m-quote" role="img" aria-label="Photo of a pale pink blossom">
    <div class="gl">We're doctors, entrepreneurs and researchers with decades of experience.<h3 class="serif">With loving support, we can blossom into our full potential.</h3></div>
    <div class="ct"><b>Contact</b>info@auvela.example<br>Terms</div>
  </div>
</div>

<!-- Desktop page -->
<div class="desktop">
  <section class="sec hero" role="img" aria-label="Photo of a white blossom on dark green leaves">
    <nav class="nav">
      <div class="logo">AUVELA</div>
      <ul><li>Enterprise</li><li>Membership</li><li class="outline">Download App</li><li style="margin-left:20px">Sign in</li></ul>
    </nav>
    <h1 class="serif">Holistic-Doctor led care<br>Pay as you like</h1>
    <p class="lede">Evidence based care with heart<br>Tailored only for you<br>Tele-Wellness</p>
    <div class="dev">Developed at Pellmoor</div>
    <span class="pill-btn">BOOK NOW</span>
  </section>

  <section class="sec trusted">
    <div class="head serif">Trusted by:&nbsp; <b>Northfield Outfitters</b></div>
    <div class="sub">Pioneers in corporate wellness: A Better Way To Grow</div>
    <div class="bubble" style="left:28px"><div class="avatar"></div><h4>Chief Strategy Officer,<br>National Tech Firm</h4><p>For the first time in 20 years of nonstop output, I found a wellness system that didn't just slow me down—it woke me up. Auvela's personalized protocols gave me energy I didn't know I was missing, and helped me show up sharper, calmer, and more focused than ever before.</p><div class="who">Daniel</div></div>
    <div class="bubble" style="left:243px"><div class="avatar"></div><h4>Operations Supervisor,<br>Regional Distribution Center</h4><p>Between shift work and stress, I was running on empty. Auvela didn't hand me a generic plan—they listened. My sleep, digestion, and moods have all leveled out. I finally feel in control of my health, and my team noticed the difference too.</p><div class="who">Jonah</div></div>
    <div class="bubble" style="left:458px"><div class="avatar"></div><h4>Warehouse Associate,<br>National Retail Chain</h4><p>I never thought wellness was made for someone like me. Auvela changed that. They spoke my language, respected my time, and helped my body stop hurting every day. It's not just medicine—it's care that fits real life.</p><div class="who">Rosalind</div></div>
    <div class="stat"><b>55</b> Million Bio-Markers analysed</div>
  </section>

  <section class="sec tested">
    <div class="ctitle serif">Time Tested and Results Driven</div>
    <div class="csub">We get it. You've tried the threads, the threads on the threads. It's time for something real—and built around you, clarity is a form of care.</div>
    <div class="cards3">
      <div class="tcard"><svg viewBox="0 0 32 32" fill="none" stroke="#f0b07c"><rect x="6" y="6" width="20" height="14" rx="2"/><path d="M4 26h24M12 13l3 3 5-6"/></svg><h4>Conflicted by fad-driven advice and<br>endless tests without real insight?</h4><p>Auvela cuts through the noise with time-tested, evidence-based care and real credentials—thousands of years of wisdom versus a few years of fragmented information in holistic medicine.</p></div>
      <div class="tcard"><svg viewBox="0 0 32 32" fill="none" stroke="#f0b07c"><rect x="8" y="10" width="16" height="18" rx="2"/><rect x="11" y="4" width="10" height="6"/><path d="M12 18h8M16 14v8"/></svg><h4>Tired of one-size-fits-all<br>supplements?</h4><p>At Auvela, every formula is tailored to your unique mind-body type. No algorithms. No shortcuts. Just real doctors creating real, time-tested protocols—just for you. We don't do "standard." Auvela formulas are hand-built by doctors to reflect your specific constitution, habits, and environment. You deserve precision—not guesswork.</p></div>
      <div class="tcard"><svg viewBox="0 0 32 32" fill="none" stroke="#f0b07c"><path d="M8 4h12l6 6v18H8z"/><path d="M12 14h10M12 19h10M12 24h6"/></svg><h4>Being overcharged by underqualified,<br>self-professed experts?</h4><p>The human psychology of valuing only that which we pay a lot for can be remedied with proven results. By setting an example—by making high-quality health care available to everyone. We hope, that most will benefit.</p></div>
    </div>
    <div class="cta"><span class="pill-btn">BOOK NOW</span><small>Three minutes. No commitment. Much clarity.</small></div>
  </section>

  <section class="sec diff">
    <div class="lt serif">The Auvela Difference</div>
    <div class="tabs3">
      <div class="tab"><span class="ic"></span><div><h5>Precision You Can<br>Trust</h5><p>Doctors cross-trained in time tested and modern science</p></div></div>
      <div class="tab"><span class="ic"></span><div><h5>Care You Can<br>Feel</h5><p>Plans crafted around your whole self &amp; labs</p></div></div>
      <div class="tab"><span class="ic"></span><div><h5>Ethics You Can Stand<br>Behind</h5><p>Fair-trade sourcing, real transparency</p></div></div>
    </div>
    <svg class="orbit" viewBox="0 0 698 694" fill="none">
      <path d="M183 267 A150 150 0 0 1 183 567" stroke="#f8c79b" stroke-width="10"/>
      <g stroke="#f8c79b" stroke-width="1">
        <path d="M268 211 H246"/><path d="M300 276 L250 292"/><path d="M346 345 L300 362"/><path d="M356 415 H334"/><path d="M342 483 L298 470"/><path d="M307 552 L262 540"/><path d="M258 619 L232 595"/>
      </g>
    </svg>
    <div class="core"><h5>1. Clinical Precision</h5><h6>What We Do</h6><p>Ayurvedic doctors trained in classical medicine and modern integrative science. Recognize interactions between herbal and pharmaceutical protocols.</p><h6>Why It Matters</h6><p>Prevents serious side effects from poor combinations (e.g., SSRIs + Brahmi, beta-blockers + Ashwagandha, blood thinners + turmeric).</p></div>
    <div class="lead"><i></i>1. Clinical Precision</div>
    <div class="node" style="left:338px;top:258px"><i></i>2. High-Touch Personalization</div>
    <div class="node" style="left:384px;top:327px"><i></i>3. No Harmful Cross-Reactions</div>
    <div class="node" style="left:394px;top:397px"><i></i>4. Science-Guided Herbalism</div>
    <div class="node" style="left:380px;top:465px"><i></i>5. Regulatory Integrity</div>
    <div class="node" style="left:345px;top:534px"><i></i>6. Global Standard Sourcing</div>
    <div class="node" style="left:276px;top:601px"><i></i>7. Evidence-Informed Guidance</div>
  </section>

  <section class="sec steps">
    <div class="rule" style="top:2px"></div>
    <div class="step" style="left:68px;top:40px"><div class="num">1</div><div><h5>Book</h5><p>Book now and fill out your secured details to be matched with a doctor specific to your needs</p></div></div>
    <div class="step" style="left:365px;top:40px"><div class="num">2</div><div><h5>Video Call</h5><p>Video chat with your specialist</p></div></div>
    <div class="step" style="left:68px;top:125px"><div class="num">3</div><div><h5>Get Care + Unlimited Text</h5><p>Get customized diet, cleanse, lifestyle exercise, yoga &amp; meditation plans by your Specialist + unlimited texting</p></div></div>
    <div class="step" style="left:365px;top:125px"><div class="num">4</div><div><h5>Monthly Video Follow Up</h5><p>Monthly video call - essential care takes persistence</p></div></div>
    <div class="rule" style="top:226px"></div>
  </section>

  <section class="sec experts">
    <div class="ctitle serif">Meet the Experts</div>
    <div class="csub">Licensed. Global. Guided by science. Every Auvela practitioner is trained in traditional medicine and modern clinical frameworks-bringing deep<br>expertise to every personalized plan.</div>
    <div class="exrow">
      <div class="excard"><div class="avatar"></div><h5>Dr. Sara Lindqvist</h5><p>MBBS<br>BAMS<br>Oncology Director</p></div>
      <div class="excard"><div class="avatar"></div><h5>Dr. Jeremiah Stowe</h5><p>MBBS<br>BAMS<br>Metabolic and<br>musculoskeletal specialist</p></div>
      <div class="excard"><div class="avatar"></div><h5>Dr. Rebecca Lin Crane</h5><p>MBBS<br>BAMS<br>Psychology specialist</p></div>
      <div class="excard"><div class="avatar"></div><h5>Dr. Anna Prestwick</h5><p>MBBS<br>BAMS<br>OBGYN and women's health</p></div>
    </div>
  </section>

  <section class="sec compare">
    <div class="lt serif">How We Compare</div>
    <div class="ls">No hidden fees, ever.</div>
    <table class="cmp-table">
      <tr><th></th><th class="brand">AUVELA</th><th>OUR<br>COMPETITORS</th><th>OTHERS</th><th>NUTRITIONIST</th><th>BIOMARKER<br>RESULTS</th><th>GENE RESULTS</th></tr>
      <tr><td class="row">Integrative Doctors</td><td class="us">Included</td><td>X</td><td>$ 500/Visit</td><td>X</td><td>X</td><td>X</td></tr>
      <tr><td class="row">1 on 1 Video</td><td class="us">Included</td><td>X</td><td>$ 500/Visit</td><td class="hi">✓</td><td>X</td><td>X</td></tr>
      <tr><td class="row">Unlimited Text</td><td class="us">Included</td><td>X</td><td>X</td><td>X</td><td>X</td><td>X</td></tr>
      <tr><td class="row">Time Tested</td><td class="us">Included</td><td>Infrequently</td><td>X</td><td>X</td><td>X</td><td>X</td></tr>
      <tr><td class="row">200 Bio marker tested</td><td class="us">1st 100 $100</td><td>100 for min<br>$300</td><td>$250/ min</td><td>X</td><td class="hi">✓</td><td>X</td></tr>
      <tr><td class="row">Usage Rate</td><td class="us">98%</td><td>20% High<br>Minimum</td><td>✓</td><td class="hi">✓</td><td class="hi">✓</td><td class="hi">✓</td></tr>
    </table>
  </section>

  <section class="sec backed">
    <h3 class="serif">Backed by Expertise. Certified for Safety. Trusted by Design.</h3>
    <div class="badges">
      <div class="badge"><div class="mk"></div>ISO 22000 &amp; EU<br>Pharmacopoeia<br>herbal standards</div>
      <div class="badge"><div class="mk" style="background:#2a3f7a"></div>GDPR-compliant<br>data privacy</div>
      <div class="badge"><div class="mk sq"></div>Every supplement<br>screened for drug<br>interactions</div>
    </div>
  </section>

  <section class="sec bio">
    <div class="chips">
      <div class="chip">Do You Need Labs for HRT?</div>
      <div class="chip on">Bio markers and holistic integration</div>
      <div class="chip">How We Personalize Every Formula</div>
      <div class="chip">Prevent contraindicated therapies with Pharmaceuticals</div>
      <div class="chip">Mislabeled Therapies to Watch Out For</div>
    </div>
    <div class="pic" role="img" aria-label="Photo of cupped hands releasing golden sparkles"></div>
    <h4>Bio markers and holistic integration</h4>
    <p>Bio markers are often not time tested nor really accurate when it comes to hormones because hormones fluctuate day to day if not hour to hour. We often don't catch imbalances or deficiencies until its far advanced and harder to treat. We employ lab bio markers along with time tested methods, often catching imbalance early on.</p>
  </section>

  <section class="sec quote" role="img" aria-label="Photo of a pale pink blossom on dark leaves">
    <div class="glass g1">
      <p>We're doctors, entrepreneurs and researchers with decades of experience.<br>Auvela is built for the soul of the modern man.</p>
      <h3 class="serif">With loving support, we can blossom into<br>our full potential.</h3>
      <span class="sig">~Founder</span>
    </div>
    <div class="qmark"></div>
    <div class="glass g2">Ten trees planted per member per month = 120 trees per year per member. Our health depends on the health of Mother Nature — trees are proven to be the #1 way to purify and nourish the environment and help avert global warming.</div>
    <div class="contact"><h3>Contact</h3><p>info@auvela.example</p><p>Terms</p></div>
  </section>

  <section class="sec foot">
    <div class="stats"><span>100% Personalized/Data Driven Formulations</span><span>|</span><span>95% Client Retention</span><span>|</span><span>3-to-12 Month Protocols</span><span>|</span><span>5M Biomarkers Studied</span></div>
    <div class="flinks"><span>Enterprise</span><span>Membership</span><span>Download App</span><span>Sign in</span></div>
    <div class="copy">© 2025 Auvela. All rights reserved.</div>
  </section>
</div>
</body>
</html>
```